Website design for management consulting firm

We need a web design for a new consulting company based in Boston, MA called "Quillmoor Ridge Consulting." This webpage will be simple home page, with a "contact us" page, that describes the services of the consulting firm. The company provides strategic planning, business assessment, process re-designs, and other management consulting functions. I would like the website to look high-tech. A logo was already created via Artsy Hive.

Target Market(s)

Other business owners across a wide spectrum of industries - from IT to retail.

Industry/Entity Type

It Company

Number of Pages Required

3 page

Colors
0455a3
ffffff

Requirements
Must have
• Front page that provides generic text / overview of the firm. A "services" tab that describes consulting services. A "contact us" tab that provides either a form to contact us or just the contact email address of the company. info@quillmoorridgeconsulting.example

```html
<!DOCTYPE html>
<html lang="en">
<head>
<meta charset="utf-8">
<title>Quillmoor Ridge Consulting</title>
<link href="https://fonts.googleapis.com/css2?family=Open+Sans:wght@400;600;700&family=Oswald:wght@500&display=swap" rel="stylesheet">
<style>
:root{
  --brand:#0455a3;
  --brand-dark:#0b3f7c;
  --navy:#0e2d55;
  --ink:#2b2b2b;
  --muted:#555;
  --footer:#3a6ba8;
  --footer-bar:#2f5e9a;
  --soft:#f2f3f5;
  --white:#fff;
}
*{box-sizing:border-box;margin:0;padding:0}
html,body{width:720px;height:1200px;overflow:hidden}
body{font-family:'Open Sans',sans-serif;color:var(--ink);background:var(--white);position:relative}
.abs{position:absolute}
.header{position:absolute;left:0;top:0;width:720px;height:80px;border-top:2px solid var(--navy);background:var(--white)}
.logo{left:60px;top:26px;display:flex;align-items:center;gap:7px}
.logo-mark{width:24px;height:28px;background:var(--brand)}
.logo-name{font-weight:700;font-size:15px;line-height:15px;color:#1d1d1d;letter-spacing:-.3px}
.logo-sub{font-size:7px;color:#1d1d1d;display:block;font-weight:400;letter-spacing:0}
.phone{left:408px;top:22px;font-size:11px;color:#333;display:flex;align-items:center;gap:4px}
.toplinks{right:60px;top:24px;font-size:8px;color:#333}
.toplinks span{margin:0 4px}
.nav{right:60px;top:50px;display:flex;gap:20px;font-size:8px;color:#222}
.nav .active{position:relative}
.nav .active svg{position:absolute;left:-5px;top:11px}
.hero{left:0;top:80px;width:720px;height:309px;background:linear-gradient(100deg,#e9edf1 0%,#8d9aac 35%,#4b5d78 60%,#2a3a55 100%)}
.hero-title{left:0;top:266px;width:720px;text-align:center;font-family:'Oswald',sans-serif;font-weight:500;font-size:17px;color:var(--white)}
.hero-text{left:0;top:291px;width:720px;text-align:center;font-size:7.5px;line-height:12px;color:var(--white)}
.arrow{top:218px}
.welcome-panel{left:60px;top:366px;width:600px;height:196px}
.video{left:93px;top:384px;width:241px;height:137px;background:linear-gradient(180deg,#3b3f46,#9aa3ad 55%,#2b2e33);border:2px solid #222}
.welcome-title{left:352px;top:384px;font-size:12.5px;font-weight:600;color:#222}
.welcome-text{left:352px;top:406px;width:292px;font-size:6.6px;line-height:12.3px;color:var(--muted)}
.btn{background:linear-gradient(#1666b5,var(--brand-dark));color:var(--white);font-size:7px;border-radius:2px;display:flex;align-items:center;justify-content:center}
.services-title{left:0;top:600px;width:720px;text-align:center;font-size:12.5px;font-weight:600;color:#333}
.service{width:150px;text-align:center;top:645px}
.service .circle{width:73px;height:73px;border-radius:50%;margin:0 auto;background:linear-gradient(#1b66b3,var(--brand-dark));display:flex;align-items:center;justify-content:center}
.service h3{font-size:9.5px;font-weight:400;color:#222;margin-top:10px;line-height:11px}
.service p{font-size:6.5px;line-height:11px;color:var(--muted);margin-top:3px}
.quick{left:59px;top:796px;width:602px;height:65px;background:var(--soft)}
.quick-label{left:13px;top:20px;font-size:11px;line-height:14.5px;color:#222}
.field{top:21px;height:23px;background:var(--white);border:1px solid #d6d6d6;font-size:6.5px;color:#777;display:flex;align-items:center;gap:6px;padding-left:6px}
.clients{left:0;top:879px;width:720px;height:128px;background:#f3f3f4}
.clients h2{position:absolute;left:0;top:33px;width:720px;text-align:center;font-size:12.5px;font-weight:600;color:#333}
.client{top:72px;font-size:15px;font-weight:600;color:#555;width:120px;text-align:center}
.footer{left:0;top:1007px;width:720px;height:157px;background:var(--footer)}
.footer-col{color:var(--white)}
.footer-col h4{font-size:6.8px;font-weight:700;letter-spacing:.2px;padding-bottom:6px;border-bottom:1px solid rgba(255,255,255,.7);width:105px;line-height:9px}
.footer-col ul{list-style:none;font-size:6.5px;line-height:14.4px;margin-top:6px}
.footer-col p{font-size:6.5px}
.footer-about{left:59px;top:1020px;width:125px;color:var(--white)}
.footer-about p{font-size:6.5px;line-height:12.4px;margin-top:9px}
.social{display:flex;gap:5px;margin-top:9px}
.social span{width:17px;height:17px;border-radius:50%;background:var(--white)}
.bottom{left:0;top:1164px;width:720px;height:36px;background:var(--footer-bar);color:var(--white);font-size:6.8px;text-align:center;line-height:36px}
</style>
</head>
<body>
<header class="header">
  <div class="abs logo"><span class="logo-mark"></span><span class="logo-name">Quillmoor Ridge<span class="logo-sub">Consulting</span></span></div>
  <div class="abs phone"><svg width="10" height="10" viewBox="0 0 24 24"><path fill="#0455a3" d="M6.6 10.8a15 15 0 0 0 6.6 6.6l2.2-2.2c.3-.3.7-.4 1-.2 1.1.4 2.3.6 3.6.6.6 0 1 .4 1 1V20c0 .6-.4 1-1 1A17 17 0 0 1 3 4c0-.6.4-1 1-1h3.5c.6 0 1 .4 1 1 0 1.3.2 2.5.6 3.6.1.3 0 .7-.2 1z"/></svg>1-800-555-0147</div>
  <div class="abs toplinks">Login<span>|</span>Register<span>|</span>Support<span>|</span>Sitemap</div>
  <nav class="abs nav">
    <span class="active">Home<svg width="34" height="6" viewBox="0 0 34 6"><path d="M1 4 Q17 0 33 4" stroke="#0455a3" stroke-width="1.2" fill="none"/></svg></span>
    <span>Services</span><span>Key Features</span><span>About Us</span><span>Help Desk</span><span>My Portal</span><span>Contact Us</span>
  </nav>
</header>

<section class="abs hero" role="img" aria-label="Photo of two businessmen in suits talking at a meeting table"></section>
<svg class="abs arrow" style="left:27px" width="12" height="34" viewBox="0 0 12 34"><path d="M11 1 1 17l10 16" stroke="#fff" fill="none"/></svg>
<svg class="abs arrow" style="left:682px" width="12" height="34" viewBox="0 0 12 34"><path d="M1 1l10 16L1 33" stroke="#fff" fill="none"/></svg>
<div class="abs hero-title">Best of Solution For IT Maintenance Contract</div>
<div class="abs hero-text">Lorem Ipsum is simply dummy text of the printing and typesetting industry.<br>Lorem Ipsum has been the industry's standard dummy text</div>

<section>
  <svg class="abs welcome-panel" viewBox="0 0 600 196" width="600" height="196">
    <path d="M0 0H600V166L300 196 0 166Z" fill="#fff" stroke="#e3e3e3"/>
  </svg>
  <div class="abs video" role="img" aria-label="Video still of business people silhouetted against a bright window">
    <svg width="237" height="133" viewBox="0 0 237 133">
      <circle cx="119" cy="67" r="15" fill="rgba(0,0,0,.55)" stroke="#fff" stroke-width="2"/>
      <path d="M114 59v16l13-8z" fill="#fff"/>
      <rect x="0" y="118" width="237" height="15" fill="#1c1c1e"/>
      <path d="M6 121v8l7-4z" fill="#fff"/>
      <text x="30" y="128" font-size="5" fill="#fff" font-family="Open Sans,sans-serif">1:38</text>
      <rect x="45" y="123" width="112" height="4" rx="2" fill="#444"/>
      <rect x="45" y="123" width="60" height="4" rx="2" fill="#2b86d8"/>
      <circle cx="105" cy="125" r="4" fill="#333" stroke="#777"/>
      <text x="160" y="128" font-size="5" fill="#fff" font-family="Open Sans,sans-serif">3:12</text>
      <rect x="178" y="120" width="16" height="11" fill="#2b6fb4"/>
      <text x="202" y="128" font-size="5" fill="#fff" font-weight="700" font-family="Open Sans,sans-serif">HD</text>
      <rect x="150" y="97" width="68" height="12" fill="#1c1c1e"/>
      <rect x="162" y="102" width="44" height="3" fill="#2b86d8"/>
    </svg>
  </div>
  <h2 class="abs welcome-title">Welcome To Quillmoor Ridge Consulting</h2>
  <p class="abs welcome-text">Lorem Ipsum is simply dummy text of the printing and typesetting industry. Lorem Ipsum has been the industry's standard dummy text ever since the 1500s, when an unknown printer took a galley of type and scrambled it to make a type specimen book. It has survived not only five centuries, but also the leap into electronic typesetting, remaining essentially unchanged. It was popularised in the 1960s with the release of Letraset sheets containing Lorem Ipsum passages. Lorem Ipsum is simply dummy text of the printing and typesetting industry.</p>
  <div class="abs btn" style="left:351px;top:498px;width:62px;height:22px">Read More</div>
</section>

<h2 class="abs services-title">Our Services</h2>
<div class="abs service" style="left:57px">
  <div class="circle"><svg width="28" height="30" viewBox="0 0 28 30" fill="#fff"><circle cx="14" cy="9" r="5"/><rect x="12" y="14" width="4" height="3"/><path d="M3 30c0-7 5-11 11-11s11 4 11 11z"/><path d="M14 0v2M5 4l2 2M23 4l-2 2M2 10h2M24 10h2" stroke="#fff" stroke-width="1.3"/></svg></div>
  <h3>Strategic Planning</h3><p>We take the time to understand<br>your business culture.</p>
</div>
<div class="abs service" style="left:208px">
  <div class="circle"><svg width="30" height="26" viewBox="0 0 30 26" fill="#fff"><rect x="1" y="12" width="5" height="13"/><rect x="8" y="4" width="5" height="21"/><circle cx="19" cy="13" r="6" fill="none" stroke="#fff" stroke-width="2.5"/><path d="M23 17l6 7" stroke="#fff" stroke-width="3"/></svg></div>
  <h3>Business Assessment</h3><p>We take the time to understand<br>your business culture.</p>
</div>
<div class="abs service" style="left:360px">
  <div class="circle"><svg width="30" height="28" viewBox="0 0 30 28" fill="none" stroke="#fff" stroke-width="3.5"><path d="M10 10l5-8 5 8"/><path d="M22 14l4 8H17"/><path d="M13 22H4l4-8"/></svg></div>
  <h3>Process Re-designs</h3><p>We take the time to understand<br>your business culture.</p>
</div>
<div class="abs service" style="left:510px">
  <div class="circle"><svg width="30" height="30" viewBox="0 0 30 30" fill="#fff"><circle cx="9" cy="5" r="3.5"/><path d="M4 10h9v10h-2v9H7v-9H4z"/><circle cx="21" cy="15" r="7.5" fill="none" stroke="#fff" stroke-width="2"/><path d="M14 15h15M21 7v16" stroke="#fff" stroke-width="1.5"/></svg></div>
  <h3>Other Management<br>Consulting</h3><p>We take the time to understand<br>your business culture.</p>
</div>

<section class="abs quick">
  <div class="abs quick-label">Quick contact<br>Form</div>
  <div class="abs field" style="left:95px;width:137px"><svg width="9" height="9" viewBox="0 0 10 10" fill="#888"><circle cx="5" cy="3" r="2.5"/><path d="M0 10c0-3 2-4.5 5-4.5s5 1.5 5 4.5z"/></svg><span style="border-left:1px solid #ddd;padding-left:5px">Enter your name</span></div>
  <div class="abs field" style="left:239px;width:137px"><svg width="10" height="8" viewBox="0 0 10 8" fill="#888"><rect width="10" height="8"/><path d="M0 0l5 4 5-4" stroke="#fff" fill="none"/></svg><span style="border-left:1px solid #ddd;padding-left:5px">Email address</span></div>
  <div class="abs field" style="left:383px;width:135px"><svg width="8" height="8" viewBox="0 0 24 24"><path fill="#888" d="M6.6 10.8a15 15 0 0 0 6.6 6.6l2.2-2.2c.3-.3.7-.4 1-.2 1.1.4 2.3.6 3.6.6.6 0 1 .4 1 1V20c0 .6-.4 1-1 1A17 17 0 0 1 3 4c0-.6.4-1 1-1h3.5c.6 0 1 .4 1 1 0 1.3.2 2.5.6 3.6.1.3 0 .7-.2 1z"/></svg>Phone number</div>
  <div class="abs btn" style="left:525px;top:21px;width:62px;height:23px">Submit</div>
</section>

<section class="abs clients">
  <h2>Our Clients</h2>
  <svg class="abs" style="left:34px;top:78px" width="8" height="14" viewBox="0 0 8 14"><path d="M7 1 1 7l6 6" stroke="#aaa" fill="none"/></svg>
  <svg class="abs" style="left:678px;top:78px" width="8" height="14" viewBox="0 0 8 14"><path d="M1 1l6 6-6 6" stroke="#aaa" fill="none"/></svg>
  <div class="abs client" style="left:50px">Norvale</div>
  <div class="abs client" style="left:173px">Brightlume</div>
  <div class="abs client" style="left:296px">Tideway</div>
  <div class="abs client" style="left:427px">Corsetta</div>
  <div class="abs client" style="left:548px">Pellix</div>
</section>

<footer class="abs footer"></footer>
<div class="abs footer-about">
  <div style="display:flex;align-items:center;gap:6px"><span style="width:18px;height:20px;background:#fff"></span><span style="font-weight:700;font-size:11px;line-height:11px">Quillmoor Ridge<span style="display:block;font-size:5px;font-weight:400">Consulting</span></span></div>
  <p>Lorem Ipsum is simply dummy text of the printing and typesetting industry. Lorem Ipsum has been the industry's standard dummy text ever since the 1500s, when an unknown printer took a galley of type and scrambled it to make a type specimen</p>
</div>
<div class="abs footer-col" style="left:235px;top:1028px">
  <h4>WELCOME</h4>
  <ul><li>Home</li><li>Services</li><li>Key Features</li><li>About Us</li><li>Help Desk</li><li>My Portal</li><li>Contact Us</li></ul>
</div>
<div class="abs footer-col" style="left:370px;top:1028px">
  <h4 style="width:90px">INFORMATION</h4>
  <ul><li>Terms &amp; Conditions</li><li>Privacy policy</li><li>Disclaimer</li><li>Sitemap</li></ul>
</div>
<div class="abs footer-col" style="left:510px;top:1028px;width:140px">
  <h4>CONTACT INFO</h4>
  <p style="line-height:12px;margin-top:10px">120 Street name, City name,<br>Country name, Zip code : 23646222.</p>
  <p style="margin-top:7px;display:flex;gap:7px;align-items:center"><svg width="7" height="7" viewBox="0 0 24 24"><path fill="#fff" d="M6.6 10.8a15 15 0 0 0 6.6 6.6l2.2-2.2c.3-.3.7-.4 1-.2 1.1.4 2.3.6 3.6.6.6 0 1 .4 1 1V20c0 .6-.4 1-1 1A17 17 0 0 1 3 4c0-.6.4-1 1-1h3.5c.6 0 1 .4 1 1 0 1.3.2 2.5.6 3.6.1.3 0 .7-.2 1z"/></svg>( 2365 ) 555 018</p>
  <p style="margin-top:6px;display:flex;gap:7px;align-items:center"><svg width="7" height="6" viewBox="0 0 10 8"><rect width="10" height="8" fill="#fff"/><path d="M0 0l5 4 5-4" stroke="#3a6ba8" fill="none"/></svg>hello@quillmoorridge.example</p>
  <div class="social"><span></span><span></span><span></span><span></span><span></span></div>
</div>
<div class="abs bottom">© 2015. quillmoorridgeconsulting.example. All rights reserved.</div>
</body>
</html>
```